Name Card Design

Looking to create a card for my business. I am a personal stylist, my business is clothes, shoes and everything to do with looking fashion forward. I help people achieve the most polished look with cloths and grooming. I would like my card to be a reflection of my qualities which are: poise, elegance, creativity and fairness.
Things I like a simple yet expensive looking, sometimes less simple but highly creative and different catches my eye. For instance I saw a card with lace trimming at the bottom, it made me think about the business that person was in. I don't like childish designs with butterflies, trees, flowers, etc.
Here is my site www.Marta-Venn.example for your perusal

On the card it should have the following info
Marta Venn
personal stylist
www.Marta-Venn.example
(+65) 842-30587
Facebook page: Ringtochic

Back of the card:
Wardrobe weeding
Personal shopping
Style consultation

Target Market(s)

mostly working women

Industry/Entity Type

Fashion

Font styles to use
Serif
Sans Serif

Requirements
Should not have
• butterflies, flowers, feathers, etc

```html
<!DOCTYPE html>
<html lang="en">
<head>
<meta charset="utf-8">
<title>Marta Venn – Personal Stylist Name Card</title>
<link rel="stylesheet" href="https://fonts.googleapis.com/css2?family=Lato:wght@300;400&family=Great+Vibes&display=swap">
<style>
  :root {
    --backdrop: #e6e2dc;
    --card-black: #141414;
    --ink-white: #f4f4f4;
    --ink-soft: #d9d9d9;
    --pattern-light: #b9b9b9;
    --pattern-mid: #7d7d7d;
    --pattern-dark: #3a3a3a;
  }
  * { box-sizing: border-box; margin: 0; padding: 0; }
  html, body {
    width: 1200px;
    height: 844px;
    overflow: hidden;
    background: var(--backdrop);
  }
  .canvas {
    position: relative;
    width: 1200px;
    height: 844px;
    display: flex;
    align-items: center;
    justify-content: center;
    gap: 44px;
  }
  .card {
    position: relative;
    width: 520px;
    height: 300px;
    background: var(--card-black);
    overflow: hidden;
    box-shadow: 0 6px 18px rgba(0,0,0,0.18);
  }
  .pattern-fill {
    position: absolute;
    background:
      radial-gradient(circle at 30% 40%, var(--pattern-light) 0%, transparent 60%),
      linear-gradient(135deg, var(--pattern-mid), var(--pattern-dark) 50%, var(--pattern-mid));
  }

  /* Front */
  .card-front .pattern-fill {
    left: 0; top: 0; width: 100%; height: 40%;
  }
  .card-front .details {
    position: absolute;
    left: 42px;
    top: 136px;
    color: var(--ink-white);
    font-family: "Lato", sans-serif;
  }
  .card-front .name {
    font-weight: 400;
    font-size: 34px;
    letter-spacing: 0.5px;
    text-transform: uppercase;
    line-height: 1;
  }
  .card-front .role {
    font-weight: 300;
    font-size: 13px;
    letter-spacing: 1.2px;
    text-transform: uppercase;
    color: var(--ink-soft);
    margin: 4px 0 0 84px;
  }
  .card-front .contacts {
    list-style: none;
    margin: 14px 0 0 84px;
    font-weight: 300;
    font-size: 14px;
    line-height: 1.55;
    color: var(--ink-soft);
  }

  /* Back */
  .card-back .pattern-fill {
    left: 0; top: 0; width: 100%; height: 100%;
  }
  .card-back .service-band {
    position: absolute;
    left: 0;
    top: 96px;
    width: 100%;
    height: 108px;
    background: var(--card-black);
    color: var(--ink-white);
    font-family: "Great Vibes", cursive;
    text-align: center;
    display: flex;
    flex-direction: column;
    justify-content: center;
    gap: 2px;
  }
  .card-back .services {
    font-size: 30px;
    line-height: 1.15;
  }
</style>
</head>
<body>
  <main class="canvas">
    <section class="card card-front">
      <div class="pattern-fill" role="img" aria-label="Black and white geometric lace-like tile pattern"></div>
      <div class="details">
        <h1 class="name">Marta Venn</h1>
        <p class="role">Personal Stylist</p>
        <ul class="contacts">
          <li>Mobile: (+65) 842-30587</li>
          <li>Email: stylist@marta-venn.example</li>
          <li>Web: www.Marta-Venn.example</li>
          <li>Facebook: Ringtochic</li>
        </ul>
      </div>
    </section>

    <section class="card card-back">
      <div class="pattern-fill" role="img" aria-label="Black and white geometric lace-like tile pattern"></div>
      <div class="service-band">
        <p class="services">Wardrobe Weeding | Personal Shopping</p>
        <p class="services">Style Consultation</p>
      </div>
    </section>
  </main>
</body>
</html>
```